Quiet Meadow Counseling business cards

Dana Korvath, LCPC, NCC
(555)347-0618
www.quietmeadowcounseling.example
dana@quietmeadowcounseling.example

Business cards. I would like it on the same background as pictured. Not on a white business card. I have attached the logo that was done by another designer with artbazaar. I am open to looking at single-sided and double-sided designs.

Target Market(s)

teenagers and adults

Industry/Entity Type

mental health

Contact Information for Business Card

Dana Korvath, LCPC, NCC (555)347-0618 dana@quietmeadowcounseling.example

Font styles to use
Other font styles liked:
• Cinzel

Colors

Designer to choose colors to be used in the design.

Requirements
Must have
• logo that is attached

```html
<!DOCTYPE html>
<html lang="en">
<head>
<meta charset="utf-8">
<title>Quiet Meadow Counseling – Business Card</title>
<link rel="stylesheet" href="https://fonts.googleapis.com/css2?family=Montserrat:wght@600&family=Arimo:wght@400;700&display=swap">
<style>
  :root {
    --bg-deep: #24323d;
    --bg-mid: #34444f;
    --bg-light: #46565f;
    --brand: #7fa2b2;
    --mark: #5f8595;
    --name: #6a8c9c;
    --contact: #9aa7ae;
    --rule: #6f8591;
  }
  * { margin: 0; padding: 0; box-sizing: border-box; }
  html, body { width: 1200px; height: 734px; overflow: hidden; }
  body { background: var(--bg-deep); }

  .card {
    position: relative;
    width: 1200px;
    height: 734px;
    background: linear-gradient(120deg, var(--bg-deep) 0%, var(--bg-mid) 55%, var(--bg-light) 100%);
    color: var(--contact);
    font-family: "Arimo", Arial, sans-serif;
  }

  .brand-mark {
    position: absolute;
    left: 524px;
    top: 70px;
    width: 180px;
    height: 180px;
    border-radius: 50%;
    background: var(--mark);
  }

  .brand-name {
    position: absolute;
    left: 0;
    width: 1200px;
    text-align: center;
    font-family: "Montserrat", Arial, sans-serif;
    font-weight: 600;
    color: var(--brand);
    line-height: 1;
  }
  .brand-name--primary { top: 372px; font-size: 76px; letter-spacing: 1px; }
  .brand-name--secondary { top: 462px; font-size: 44px; letter-spacing: 5px; }

  .practitioner {
    position: absolute;
    left: 0;
    width: 1200px;
    top: 527px;
    text-align: center;
    font-weight: 700;
    font-size: 38px;
    letter-spacing: 1px;
    color: var(--name);
  }

  .divider {
    position: absolute;
    left: 51px;
    top: 588px;
    width: 1101px;
    height: 2px;
    background: var(--rule);
  }

  .contact {
    position: absolute;
    display: flex;
    align-items: center;
    font-size: 31px;
    line-height: 1;
    color: var(--contact);
  }
  .contact svg { flex: none; stroke: var(--contact); fill: none; stroke-width: 2; }
  .contact--phone { left: 48px; top: 612px; gap: 28px; }
  .contact--email { right: 52px; top: 612px; gap: 30px; }
  .contact--web { right: 52px; top: 662px; gap: 30px; }
</style>
</head>
<body>
  <main class="card">
    <div class="brand-mark" aria-hidden="true"></div>
    <div class="brand-name brand-name--primary">QUIET MEADOW</div>
    <div class="brand-name brand-name--secondary">COUNSELING</div>

    <div class="practitioner">Dana Korvath, LCPC, NCC</div>
    <div class="divider"></div>

    <div class="contact contact--phone">
      <svg width="34" height="34" viewBox="0 0 24 24" aria-hidden="true">
        <path d="M5 3h3l2 5-2 1.5a11 11 0 0 0 6.5 6.5L16 14l5 2v3a2 2 0 0 1-2 2A17 17 0 0 1 3 5a2 2 0 0 1 2-2z"/>
        <path d="M14 3a7 7 0 0 1 7 7M14 6.5a3.5 3.5 0 0 1 3.5 3.5"/>
      </svg>
      <span>(555)347-0618</span>
    </div>

    <div class="contact contact--email">
      <span>dana@quietmeadowcounseling.example</span>
      <svg width="46" height="32" viewBox="0 0 30 20" aria-hidden="true">
        <rect x="1" y="1" width="28" height="18" rx="1"/>
        <path d="M1 1l14 10L29 1M1 19l10-9M29 19l-10-9"/>
      </svg>
    </div>

    <div class="contact contact--web">
      <span>www.quietmeadowcounseling.example</span>
      <svg width="46" height="40" viewBox="0 0 24 24" aria-hidden="true">
        <circle cx="12" cy="12" r="10"/>
        <ellipse cx="12" cy="12" rx="4.5" ry="10"/>
        <path d="M2 12h20M4 6.5h16M4 17.5h16"/>
      </svg>
    </div>
  </main>
</body>
</html>
```